Dalworth Construction Needs a Business Card

Our current business card is very bland, and since we have a new logo, we would like a new business card design to reflect our company. It can be a single-sided or two-sided card, but it is important that our contact information appears on the same side. I am attaching a copy of our old card and our new logo. If you need the logo in another format than the one I'm sending, please let me know. This is the information that we must have on our card, but not necessarily in any specific order:
1) Our logo
2) General Contractor
3) Grant Ellsworth, Owner
4) 482 Commerce Loop Road, Brackenford, Westmoor 40718
5) Office: 555-418-7735
7) Fax: 555-418-7736
8) Cell: 555-609-4418
9) dalworthconstruction@qvx.net
10) dalworthconstruction.com (can be omitted if necessary)
Also, I will need files in a format that I can alter if any of the above information changes in the near future. Thank you in advance for your submissions!
Target Market(s)
Commercial and residential clients, architects, and subcontractors.
Industry/Entity Type
Business
Look and feel

```html
<!DOCTYPE html>
<html lang="en">
<head>
<meta charset="utf-8">
<title>Dalworth Construction – Business Card</title>
<link rel="stylesheet" href="https://fonts.googleapis.com/css2?family=Crimson+Text:wght@400;600&display=swap">
<style>
  :root {
    --backdrop: #1c1c1c;
    --card-light: #8d8985;
    --card-dark: #555250;
    --mark: #3b383b;
    --accent: #f6c733;
    --accent-deep: #e3ae1f;
    --ink: #141414;
  }
  * { box-sizing: border-box; margin: 0; padding: 0; }
  html, body {
    width: 1200px;
    height: 900px;
    overflow: hidden;
    background: var(--backdrop);
  }
  .card {
    position: absolute;
    left: 100px;
    top: 73px;
    width: 1000px;
    height: 754px;
    overflow: hidden;
    background: linear-gradient(160deg, var(--card-light) 0%, #6f6c69 45%, var(--card-dark) 100%);
    font-family: "Crimson Text", Georgia, serif;
  }
  .accent-shape {
    position: absolute;
    inset: 0;
    width: 100%;
    height: 100%;
  }
  .brand {
    position: absolute;
    left: 44px;
    top: 52px;
    display: flex;
    align-items: center;
    gap: 30px;
  }
  .brand-square {
    width: 200px;
    height: 192px;
    background: var(--mark);
  }
  .brand-name {
    color: var(--mark);
    font-weight: 600;
    line-height: 1;
    text-transform: uppercase;
  }
  .brand-name .line-main {
    display: block;
    font-size: 104px;
    letter-spacing: 2px;
  }
  .brand-name .line-sub {
    display: block;
    font-size: 44px;
    letter-spacing: 16px;
    margin-top: 6px;
  }
  .contact {
    position: absolute;
    left: 40px;
    top: 298px;
    list-style: none;
    color: var(--ink);
    font-size: 34px;
    line-height: 35px;
  }
  .contact .person { color: var(--accent); }
  .shape-name {
    position: absolute;
    left: 600px;
    top: 470px;
    color: var(--accent-deep);
    font-weight: 600;
    font-size: 44px;
    line-height: 1;
    text-transform: uppercase;
    letter-spacing: 1px;
  }
</style>
</head>
<body>
  <main class="card">
    <svg class="accent-shape" viewBox="0 0 574 433" preserveAspectRatio="none" aria-hidden="true">
      <path d="M229,430 C300,330 420,172 535,167 C568,166 574,200 574,240 L574,398 C560,426 520,433 480,433 C400,431 300,424 229,430 Z" fill="var(--accent)"/>
    </svg>

    <header class="brand">
      <div class="brand-square"></div>
      <div class="brand-name">
        <span class="line-main">Dalworth</span>
        <span class="line-sub">Construction</span>
      </div>
    </header>

    <ul class="contact">
      <li class="person">Grant Ellsworth</li>
      <li>General Contractor</li>
      <li>482 Commerce Loop Road,</li>
      <li>Brackenford, Westmoor 40718</li>
      <li>Office: (555)418-7735</li>
      <li>Fax: (555)418-7736</li>
      <li>Cell: (555)609-4418</li>
      <li>dalworthconstruction@qvx.net</li>
      <li>www.dalworthconstruction.com</li>
    </ul>

    <div class="shape-name">Dalworth</div>
  </main>
</body>
</html>
```